Velmora - New coded website

Current website is around 5 years old and corrupted in some ways...
I would like to refresh the design and to create a new coded website based on the current content .
Please refer to :
www.velmora-sample.com.au

Coded - Design and coding required

```html
<!DOCTYPE html>
<html lang="en">
<head>
<meta charset="utf-8">
<title>Velmora – Odours Controlled Naturally</title>
<link href="https://fonts.googleapis.com/css2?family=Barlow:ital,wght@0,300;0,400;0,500;0,600;0,700;1,400&display=swap" rel="stylesheet">
<style>
:root{
  --navy:#05212d;
  --teal:#00546e;
  --green:#72b841;
  --lime:#83c853;
  --mist:#eff4f6;
  --board:#e6ebef;
  --page:#f3f7f9;
  --text:#1c2f38;
  --muted:#6c7c84;
}
*{box-sizing:border-box;margin:0;padding:0}
html,body{width:1200px;height:3013px;overflow:hidden}
body{background:var(--board);font-family:'Barlow',sans-serif;color:var(--text);position:relative}
.abs{position:absolute}

/* style guide */
.brand-mark{left:204px;top:132px;display:flex;align-items:center;gap:12px}
.brand-mark .dot{width:48px;height:48px;border-radius:50%;background:var(--green)}
.brand-mark .name{font-size:36px;font-weight:400;color:var(--navy);letter-spacing:-.5px}
.guide-title{font-size:26px;font-weight:400;color:var(--navy)}
.guide-fonts{left:570px;top:100px}
.guide-fonts p{font-size:15px;color:#44545c;margin-top:18px}
.guide-colors{left:787px;top:100px}
.swatches{display:flex;gap:10px;margin-top:12px}
.swatch{width:42px;text-align:center;font-size:10px;color:#5c6c74}
.swatch i{display:block;width:42px;height:42px;border-radius:50%;margin-bottom:8px}

/* site */
.site{left:226px;top:275px;width:784px;height:2632px;background:var(--page);overflow:hidden}
.section{position:absolute;left:0;width:784px}

.hero{top:0;height:298px;background:linear-gradient(180deg,#1f3a2b 0%,#264a2c 30%,#0f3140 70%,var(--navy) 100%)}
.nav{position:absolute;left:0;top:0;width:100%;height:44px;display:flex;align-items:center;padding:0 46px}
.nav .logo{display:flex;align-items:center;gap:6px;color:#fff;font-size:16px;font-weight:500}
.nav .logo i{width:18px;height:18px;border-radius:50%;background:var(--green)}
.nav ul{list-style:none;display:flex;gap:22px;margin-left:64px;font-size:8px;color:#fff;font-weight:500}
.btn{background:var(--green);color:#fff;font-weight:600;font-size:8px;text-transform:uppercase;display:inline-block}
.nav .btn{margin-left:auto;padding:8px 10px}
.hero h1{position:absolute;left:46px;top:190px;font-size:29px;line-height:1.12;font-weight:600;color:#fff}
.hero h1 span{color:var(--lime)}
.hero .arrow{position:absolute;left:372px;top:216px}
.hero p{position:absolute;left:483px;top:193px;width:262px;font-size:8px;line-height:1.75;color:#c6d3d8}
.hero p b{color:#fff;font-weight:600}

.cards{top:304px;height:192px;display:flex;gap:5px}
.card{position:relative;width:192px;height:192px;background:linear-gradient(180deg,#3d5560,#16323d)}
.card span{position:absolute;bottom:22px;left:0;right:0;display:flex;justify-content:center;align-items:center;gap:7px;color:#fff;font-size:10px;font-weight:500}
.go{width:24px;height:24px;border-radius:50%;background:var(--green);display:inline-flex;align-items:center;justify-content:center}
.card.ask{background:linear-gradient(160deg,#8fd05f,var(--green))}
.card.ask h4{position:absolute;top:124px;width:100%;text-align:center;color:#fff;font-size:10px;font-weight:600}
.card.ask .light{position:absolute;top:144px;left:56px;width:82px;height:26px;background:#fff;color:var(--green);font-size:7px;font-weight:600;display:flex;align-items:center;justify-content:center}

.intro{top:540px;text-align:center;font-size:20.5px;line-height:1.18;color:var(--navy);font-weight:500}
.intro span{color:var(--teal)}

.about{top:655px;height:331px;background:var(--mist)}
.photo{position:absolute;background:linear-gradient(180deg,#7d8f96,#3f5a4f)}
.badge{position:absolute;left:165px;top:142px;width:106px;height:53px;background:var(--green);color:#fff;display:flex;align-items:center;justify-content:center;gap:6px}
.badge b{font-size:24px;font-weight:600}
.badge small{font-size:8px;line-height:1.1}
.eyebrow{font-size:6.5px;letter-spacing:2px;color:var(--green);text-transform:uppercase;font-weight:500}
.about .copy{position:absolute;left:447px;top:60px;width:240px}
.about h2{font-size:24px;line-height:1.05;font-weight:300;color:var(--navy);margin-top:6px}
.about h2 b{font-weight:600}
.about p{font-size:7.6px;line-height:1.75;color:var(--muted);margin-top:14px}
.link{font-size:7.5px;font-weight:600;color:var(--navy);border-bottom:1px solid var(--navy);display:inline-block;margin-top:18px}

.features{top:1040px;text-align:center}
.features h2,.projects h2{font-size:25px;font-weight:300;color:var(--navy);margin-top:6px}
.features h2 b,.projects h2 b{font-weight:600}
.feat-list{display:flex;justify-content:space-between;width:580px;margin:26px auto 0;text-align:left}
.feat{display:flex;align-items:center;gap:8px;font-size:9px;color:var(--text);line-height:1.2}

.banner{top:1179px;height:274px;background:linear-gradient(90deg,#2b3e42 0%,#20373f 45%,var(--navy) 75%)}
.banner h2{position:absolute;left:481px;top:82px;font-size:25px;line-height:1.0;font-weight:300;color:#fff}
.banner h2 b{font-weight:600}
.banner .play{position:absolute;left:483px;top:171px;display:flex;align-items:center;gap:12px;color:#fff;font-size:8px;font-weight:600}
.banner .play i{width:34px;height:34px;border-radius:50%;background:var(--green);display:flex;align-items:center;justify-content:center}
.banner .play span{border-bottom:1px solid #fff}

.projects{top:1503px;text-align:center}
.proj-grid{position:absolute;left:102px;top:61px;display:flex;gap:15px;text-align:left}
.proj{width:282px;height:258px;background:var(--mist)}
.proj .pic{height:182px;background:linear-gradient(180deg,#6d6a5a,#4f6a5a 60%,#5b6d62)}
.proj .pic.alt{background:linear-gradient(180deg,#8ea6c0,#4d5a4a 60%,#3b4338)}
.proj .meta{position:relative;padding:14px 14px 0}
.proj small{font-size:6px;color:var(--muted)}
.proj h5{font-size:10px;font-weight:400;color:var(--navy);line-height:1.25;margin-top:3px;width:165px}
.proj .go{position:absolute;right:14px;top:26px}
.projects .link{position:absolute;left:361px;top:343px;font-size:7px;color:var(--teal);border-color:var(--teal)}

.quote{top:1907px;height:272px;background:linear-gradient(90deg,var(--page) 30%,#dde7dd 80%,#c9d9c3)}
.quote .inner{position:absolute;left:230px;top:50px;width:282px;text-align:center}
.quote h3{font-size:17px;font-weight:400;line-height:1.2;color:var(--navy);margin-top:12px}
.quote p{font-size:7px;font-style:italic;line-height:1.9;color:var(--muted);margin-top:14px}
.quote .who{font-size:7px;color:var(--teal);margin-top:16px}

.partners{top:2225px;height:30px}
.partner{position:absolute;top:0;height:26px;background:#c5cdd2;border-radius:3px}

.footer{top:2300px;height:332px;background:var(--navy);color:#fff}
.footer .logo{position:absolute;left:49px;top:50px;display:flex;align-items:center;gap:6px;font-size:19px;font-weight:500}
.footer .logo i{width:24px;height:24px;border-radius:50%;background:var(--green)}
.footer .about-f{position:absolute;left:49px;top:88px;width:150px;font-size:7px;line-height:1.7;color:#c4cfd3}
.footer .social{position:absolute;left:49px;top:125px;width:14px;height:14px;border-radius:50%;background:var(--green)}
.footer .copy{position:absolute;left:49px;top:148px;font-size:6px;color:#c4cfd3}
.news{position:absolute;left:350px;top:61px;width:384px;height:97px;background:#0b2c3a;padding:24px 24px 0}
.news h4{font-size:14px;font-weight:500}
.news .field{display:flex;align-items:flex-end;gap:10px;margin-top:6px}
.news .field span{flex:1;font-size:6px;color:#9aaab0;border-bottom:1px solid #5b727b;padding-bottom:4px}
.news .btn{padding:8px 18px;font-size:6.5px}
.fcol{position:absolute;top:190px;font-size:6.5px;color:#aab8bd;line-height:2.5}
.fcol h6{font-size:9px;font-weight:600;color:#fff;margin-bottom:4px}
</style>
</head>
<body>

<div class="abs brand-mark"><i class="dot"></i><span class="name">Velmora</span></div>

<div class="abs guide-fonts">
  <div class="guide-title">Fonts:</div>
  <p>Barlow</p>
</div>

<div class="abs guide-colors">
  <div class="guide-title">Colors:</div>
  <div class="swatches">
    <div class="swatch"><i style="background:var(--navy)"></i>#05212d</div>
    <div class="swatch"><i style="background:var(--teal)"></i>#00546e</div>
    <div class="swatch"><i style="background:var(--green)"></i>#72b841</div>
    <div class="swatch"><i style="background:var(--lime)"></i>#83c853</div>
    <div class="swatch"><i style="background:var(--mist)"></i>#eff4f6</div>
  </div>
</div>

<main class="abs site">

  <section class="section hero" role="img" aria-label="Photo of a person with open arms in a green field">
    <nav class="nav">
      <div class="logo"><i></i>Velmora</div>
      <ul><li>About Us</li><li>Products</li><li>How Biofiltration Works</li><li>Industries</li><li>Past Projects</li><li>Contact</li></ul>
      <span class="btn">Request a Quote</span>
    </nav>
    <h1>Odours <span>Controlled</span><br>Naturally</h1>
    <svg class="arrow" width="14" height="10" viewBox="0 0 14 10"><path d="M1 5h11M8 1l4 4-4 4" stroke="#fff" stroke-width="1.2" fill="none"/></svg>
    <p>Velmora produces a comprehensive range of engineered, highly efficient and cost-effective odour control systems specifically designed and developed for <b>removal and corrosion</b> prevention for municipal and industrial applications.</p>
  </section>

  <section class="section cards">
    <div class="card" role="img" aria-label="Photo of biofilter tanks"><span>Products <i class="go"><svg width="10" height="8" viewBox="0 0 10 8"><path d="M1 4h7M5.5 1.5 8 4 5.5 6.5" stroke="#fff" fill="none"/></svg></i></span></div>
    <div class="card" role="img" aria-label="Photo of an odour control unit"><span>Features <i class="go"><svg width="10" height="8" viewBox="0 0 10 8"><path d="M1 4h7M5.5 1.5 8 4 5.5 6.5" stroke="#fff" fill="none"/></svg></i></span></div>
    <div class="card" role="img" aria-label="Photo of an industrial biofilter bed"><span>Industries <i class="go"><svg width="10" height="8" viewBox="0 0 10 8"><path d="M1 4h7M5.5 1.5 8 4 5.5 6.5" stroke="#fff" fill="none"/></svg></i></span></div>
    <div class="card ask"><h4>Got a Question?</h4><span class="light">LET US KNOW</span></div>
  </section>

  <p class="section intro">Velmora uses <span>sustainable biotechnology</span> to resolve odour and<br>corrosion problems in a highly efficient, environmentally friendly<br>and cost-effective manner.</p>

  <section class="section about">
    <div class="photo" style="left:102px;top:50px;width:233px;height:109px" role="img" aria-label="Photo of green biofilter tanks"></div>
    <div class="photo" style="left:102px;top:175px;width:233px;height:109px;background:linear-gradient(180deg,#6f8a63,#8a9a86)" role="img" aria-label="Aerial photo of an installed biofilter site"></div>
    <div class="badge"><b>20+</b><small>Years of<br>Experience</small></div>
    <div class="copy">
      <div class="eyebrow">About Velmora</div>
      <h2>The Odour<br><b>Control Solutions</b></h2>
      <p>Velmora's unique product designs were created when company founder, Marcus Hale was working at the Regional Water Authority.</p>
      <p>Frustrated with the issues encountered with the wide-spread use of outdoor biofilter beds and the expensive and negative environmental effects of other odour treatment solutions, he designed a unique, tiered biofilter which is fully enclosed to allow for the best control over system operating conditions.</p>
      <span class="link">Discover More</span>
    </div>
  </section>

  <section class="section features">
    <div class="eyebrow">Velmora Features</div>
    <h2>What Makes Us <b>The Best</b></h2>
    <div class="feat-list">
      <div class="feat"><svg width="28" height="28" viewBox="0 0 28 28" fill="none" stroke="#72b841" stroke-width="1.2"><circle cx="14" cy="12" r="6"/><path d="M14 2v3M14 19v3M4 12h3M21 12h3M4 25h20"/></svg>Biological &amp;<br>Sustainable Technology</div>
      <div class="feat"><svg width="28" height="28" viewBox="0 0 28 28" fill="none" stroke="#72b841" stroke-width="1.2"><path d="M4 24 16 12M18 4l6 6-6 6-6-6z"/></svg>Efficient<br>Maintenance Cost</div>
      <div class="feat"><svg width="30" height="28" viewBox="0 0 30 28" fill="none" stroke="#72b841" stroke-width="1.2"><path d="M3 12 10 6l8 1 6-3 4 7-3 9-8 3-4-4-8 1z"/></svg>100%<br>Australian Owned</div>
      <div class="feat"><svg width="28" height="28" viewBox="0 0 28 28" fill="none" stroke="#72b841" stroke-width="1.2"><circle cx="14" cy="14" r="12"/><path d="M14 7c5 3 5 10 0 14-5-4-5-11 0-14zM14 10v11"/></svg>Eco<br>Friendly</div>
    </div>
  </section>

  <section class="section banner" role="img" aria-label="Photo of an installed odour control system beside water tanks">
    <h2>Get the <b>Fastest,<br>Easiest &amp; Efficient</b><br>Installation Today</h2>
    <div class="play"><i><svg width="10" height="12" viewBox="0 0 10 12"><path d="M1 1l8 5-8 5z" fill="#fff"/></svg></i><span>GET A QUOTE</span></div>
  </section>

  <section class="section projects">
    <div class="eyebrow">Our Work</div>
    <h2>Past <b>Projects</b></h2>
    <div class="proj-grid">
      <article class="proj">
        <div class="pic" role="img" aria-label="Photo of biofilter tanks at a pump station"></div>
        <div class="meta"><small>3000 M3/H-H2S 250PPM</small><h5>Lindell Street Pump Station: Preventing Odours and Corrosion in Water Infrastructure</h5><i class="go"><svg width="10" height="8" viewBox="0 0 10 8"><path d="M1 4h7M5.5 1.5 8 4 5.5 6.5" stroke="#fff" fill="none"/></svg></i></div>
      </article>
      <article class="proj">
        <div class="pic alt" role="img" aria-label="Photo of a fenced treatment plant"></div>
        <div class="meta" style="padding-top:20px"><small>6750 M3/H-H2S 35PPM</small><h5>Ashby Road WWPS Odour Treatment Plant</h5><i class="go" style="top:26px"><svg width="10" height="8" viewBox="0 0 10 8"><path d="M1 4h7M5.5 1.5 8 4 5.5 6.5" stroke="#fff" fill="none"/></svg></i></div>
      </article>
    </div>
    <span class="link">View All Projects</span>
  </section>

  <section class="section quote" role="img" aria-label="Soft photo of a person resting on a grassy hillside">
    <div class="inner">
      <svg width="24" height="18" viewBox="0 0 24 18"><path d="M0 0h10v9l-4 9H2l3-8H0zM13 0h10v9l-4 9h-4l3-8h-5z" fill="#72b841"/></svg>
      <h3>As soon as the system was started,<br>the smell disappeared!</h3>
      <p>"Marcus and Velmora team promised to stop the odour from our smelly neighbor and they delivered- in spades! As soon as the system was started, the smell disappeared. The system is well designed, very professionally installed and the beauty of it is, apart from a constantly running fan, it is bacteria doing the heavy lifting, so it is very environmentally friendly."</p>
      <div class="who">Tom Brennan</div>
    </div>
  </section>

  <section class="section partners">
    <i class="partner" style="left:102px;width:85px"></i>
    <i class="partner" style="left:238px;width:61px"></i>
    <i class="partner" style="left:348px;width:85px"></i>
    <i class="partner" style="left:484px;width:64px"></i>
    <i class="partner" style="left:597px;width:85px"></i>
  </section>

  <footer class="section footer">
    <div class="logo"><i></i>Velmora</div>
    <p class="about-f">Velmora uses sustainable biotechnology, innovatively engineered to resolve odour and corrosion problems.</p>
    <i class="social"></i>
    <p class="copy">© 2023 Velmora · Crafted by Studio Nine</p>
    <div class="news">
      <h4>Stay Updated</h4>
      <div class="field"><span>Enter Your Email Address</span><b class="btn">Subscribe</b></div>
    </div>
    <div class="fcol" style="left:350px"><h6>- Quick Links</h6>Odour Control Products<br>How Biofiltration Works<br>Odour Control by Industry<br>Past Projects<br>About Us</div>
    <div class="fcol" style="left:502px"><h6>- Information</h6>Sitemap<br>Privacy Policy<br>ABN: 00 000 000 000</div>
    <div class="fcol" style="left:639px"><h6>- Contact Info</h6>+61 (08) 5550 0123<br><span style="line-height:1.4;display:block">12 Sample Way,<br>Westfield WA 6000, Australia</span></div>
  </footer>

</main>
</body>
</html>
```